Nur Briefpapier und VK für Pflegedienst, Logo vorhanden!!!!
Zielgruppe
Wir sind ein Pflegedienst, unsere Zielgruppe sind Krankenkassen und Patienten und andere Krankenhäuser mit denen wir zusammen arbeiten.
Aufgabenstellung
modern, seriös, elitär

```html
<!DOCTYPE html>
<html lang="de">
<head>
<meta charset="utf-8">
<title>Fenrokare Pflegedienste – Briefpapier und Visitenkarten</title>
<link rel="stylesheet" href="https://fonts.googleapis.com/css2?family=Source+Sans+3:wght@400;600&display=swap">
<style>
  :root {
    --backdrop: #d2d5d7;
    --paper: #ffffff;
    --brand-red: #e11d27;
    --brand-red-deep: #c1222e;
    --ink-red: #d81e28;
  }
  * { margin: 0; padding: 0; box-sizing: border-box; }
  html, body {
    width: 1200px; height: 1093px; overflow: hidden;
    background: var(--backdrop);
    font-family: "Source Sans 3", sans-serif;
    color: var(--ink-red);
  }
  .stationery { position: relative; width: 1200px; height: 1093px; }

  .letter-back {
    position: absolute; left: 266px; top: 202px;
    width: 450px; height: 636px;
    background: var(--brand-red-deep);
  }
  .letter {
    position: absolute; left: 309px; top: 241px;
    width: 450px; height: 637px;
    background: var(--paper);
  }
  .letter::after {
    content: ""; position: absolute; left: 0; right: 0; bottom: 0;
    height: 6px; background: var(--brand-red);
  }
  .brand-mark {
    display: flex; align-items: center; gap: 3px;
    font-weight: 600; color: var(--brand-red);
    line-height: 1;
  }
  .brand-mark .square { width: 7px; height: 7px; background: currentColor; }
  .letter .brand-mark { position: absolute; left: 196px; top: 34px; font-size: 13px; }

  .letter-sender {
    position: absolute; left: 39px; top: 96px;
    font-size: 3.6px; white-space: nowrap;
  }
  .letter-contact {
    position: absolute; left: 326px; top: 25px;
    font-size: 6.3px; line-height: 8.3px;
  }
  .letter-contact p { margin-bottom: 8.3px; }
  .letter-contact strong { font-weight: 600; }

  .card {
    position: absolute; left: 791px;
    width: 182px; height: 118px;
  }
  .card-front {
    top: 501px; background: var(--brand-red);
    display: flex; align-items: center; justify-content: center;
  }
  .card-front .brand-mark { color: var(--paper); font-size: 22px; gap: 5px; }
  .card-front .brand-mark .square { width: 11px; height: 11px; }

  .card-back { top: 642px; background: var(--paper); }
  .card-back::after {
    content: ""; position: absolute; left: 0; right: 0; bottom: 0;
    height: 5px; background: var(--brand-red);
  }
  .card-back .brand-mark { position: absolute; left: 14px; top: 24px; font-size: 8px; gap: 2px; }
  .card-back .brand-mark .square { width: 4px; height: 4px; }
  .card-details {
    position: absolute; left: 71px; top: 20px;
    font-size: 4.2px; line-height: 5.8px;
  }
  .card-details .person { font-size: 5.6px; line-height: 5.8px; margin-bottom: 8px; }
  .card-details .person strong { font-weight: 600; }
  .card-details p { margin-bottom: 6px; }
</style>
</head>
<body>
<main class="stationery">
  <div class="letter-back"></div>

  <section class="letter" aria-label="Briefpapier">
    <div class="brand-mark"><span class="square"></span>Fenrokare</div>
    <div class="letter-sender">Fenrokare Pflegedienste | Musterstraße 12–14 | 12345 Musterstadt</div>
    <div class="letter-contact">
      <p><strong>Pflegedienste Fenrokare</strong><br>Musterstraße 12–14<br>12345 Musterstadt</p>
      <p>T 01234 / 123 456 789<br>F 01234 / 123 456 789</p>
      <p>info@fenrokare-pflegedienste.de<br>www.fenrokare-pflegedienste.de</p>
      <p>Bankverbindung<br>IBAN DEXX 0000 0000 0000 0000</p>
      <p>Bürozeiten<br>Mo–Fr: 09:00 – 17:00 Uhr</p>
    </div>
  </section>

  <section class="card card-front" aria-label="Visitenkarte Vorderseite">
    <div class="brand-mark"><span class="square"></span>Fenrokare</div>
  </section>

  <section class="card card-back" aria-label="Visitenkarte Rückseite">
    <div class="brand-mark"><span class="square"></span>Fenrokare</div>
    <div class="card-details">
      <div class="person"><strong>Max Mustermann</strong><br>Pflegedienstleiter</div>
      <p>Musterstraße 12–14 | 12345 Musterstadt</p>
      <p>T 01234 / 123 456 789<br>F 01234 / 123 456 789</p>
      <p>info@fenrokare-pflegedienste.de<br>www.fenrokare-pflegedienste.de</p>
    </div>
  </section>
</main>
</body>
</html>
```